Powerpoint Presentation design template

I am looking for a PPT presentation that show class and professionalism and in the same colour them as the logo. It should be simple, but yet classy and pro. The business is an oil and gas exploration and exploitation business. The business has nothing to do with solar panel and other renewable energies, so please no solar panel or wind farms in the background. It would be more oil rigs and LNG plant in the background of some slide templates...

oil and gas exploration and exploitation

```html
<!DOCTYPE html>
<html lang="en">
<head>
<meta charset="utf-8">
<title>Navaro Energy – Presentation Template</title>
<link href="https://fonts.googleapis.com/css2?family=Poppins:wght@500;600;700&family=Open+Sans:wght@400;600&display=swap" rel="stylesheet">
<style>
  :root{
    --navy:#0c1f66;
    --navy-deep:#0a1a55;
    --blue:#0b8fd6;
    --teal:#23a58f;
    --text:#5a6173;
    --page:#ffffff;
    --slide:#ffffff;
  }
  *{box-sizing:border-box;margin:0;padding:0}
  html,body{width:1200px;height:3996px;overflow:hidden;background:var(--page)}
  body{position:relative;font-family:"Open Sans",Arial,sans-serif;color:var(--text)}
  .slide{position:absolute;left:71px;width:1047px;height:589px;background:var(--slide);overflow:hidden;
    box-shadow:0 14px 30px rgba(20,30,60,.18)}
  .photo{position:absolute}
  h2{font-family:"Poppins",Arial,sans-serif;font-weight:700;color:var(--navy);font-size:28px;line-height:38px}
  p.body{font-size:12.2px;line-height:23px;margin-top:14px}
  .stats{display:flex;gap:86px;margin-top:18px}
  .stat b{display:block;font-family:"Poppins",Arial,sans-serif;font-weight:600;color:var(--blue);font-size:34px;line-height:38px}
  .stat span{display:block;font-family:"Poppins",Arial,sans-serif;font-weight:600;color:var(--navy);font-size:14px;margin-top:4px}
  .badge{position:absolute;border-radius:50%;background:var(--blue);display:flex;align-items:center;justify-content:center}

  /* cover */
  .cover{top:74px}
  .cover .photo{inset:0;background:linear-gradient(180deg,#5d74a3 0%,#3d5189 45%,#1d2c6e 80%,#0d1a57 100%)}
  .brand{position:absolute;left:355px;top:252px;display:flex;align-items:center;gap:18px}
  .brand i{width:86px;height:86px;border-radius:50%;background:#fff;display:block}
  .brand span{font-family:"Poppins",Arial,sans-serif;font-weight:700;color:#fff;font-size:44px;letter-spacing:1px}

  /* why choose */
  .why{top:715px}
  .why .photo{left:0;top:0;width:452px;height:589px;background:linear-gradient(180deg,#b9cbdc 0%,#8c9eb0 45%,#6a6a62 75%,#4a4d52 100%)}
  .why .bar{position:absolute;left:452px;top:0;width:25px;height:589px;background:var(--navy-deep)}
  .why .copy{position:absolute;left:522px;top:86px;width:460px}
  .why .copy p.note{margin-top:18px}

  /* drilling */
  .drill{top:1356px}
  .drill .p1{left:0;top:0;width:246px;height:589px;background:linear-gradient(180deg,#9fb6cc 0%,#8494a6 45%,#6b5a55 75%,#3f4b55 100%)}
  .drill .p2{left:262px;top:0;width:186px;height:484px;background:linear-gradient(180deg,#a5bbd0 0%,#8b9bab 50%,#7a5e58 85%,#5a5f66 100%)}
  .drill .badge{left:212px;top:423px;width:154px;height:154px}
  .drill .copy{position:absolute;left:495px;top:87px;width:470px}

  /* safety */
  .safety{top:1997px}
  .safety .p1{left:0;top:0;width:372px;height:500px;background:linear-gradient(160deg,#3e3b4a 0%,#c2572d 45%,#e98a3e 70%,#5a3a33 100%)}
  .safety .p2{left:106px;top:103px;width:372px;height:486px;border-left:10px solid #fff;border-top:10px solid #fff;background:linear-gradient(170deg,#4a4252 0%,#d1622f 40%,#f0973f 55%,#5d4a44 80%,#2f2d33 100%)}
  .safety .copy{position:absolute;left:550px;top:73px;width:420px}
  .ticks{list-style:none;margin-top:22px}
  .ticks li{display:flex;align-items:center;gap:16px;font-family:"Poppins",Arial,sans-serif;font-weight:600;font-size:12px;color:var(--navy);margin-bottom:22px}

  /* downstream */
  .down{top:2636px}
  .down .head{position:absolute;left:0;top:70px;width:100%;text-align:center}
  .down .head p{font-size:12.2px;line-height:23px;width:880px;margin:14px auto 0}
  .down .photo{left:0;top:238px;width:546px;height:351px;background:linear-gradient(135deg,#1f2e3c 0%,#3d5566 40%,#7a6a4c 60%,#24323d 100%)}
  .down .copy{position:absolute;left:610px;top:253px;width:380px}
  .down h3{font-family:"Poppins",Arial,sans-serif;font-weight:600;color:var(--navy);font-size:20px}
  .down .copy p{font-size:14px;line-height:28px;margin-top:8px}
  .checks{list-style:none;margin-top:20px}
  .checks li{display:flex;align-items:center;gap:12px;font-family:"Poppins",Arial,sans-serif;font-weight:600;font-size:14px;color:var(--navy);margin-bottom:24px}

  /* equipment */
  .equip{top:3277px}
  .equip .photo{left:589px;top:0;width:458px;height:589px;background:linear-gradient(180deg,#b9cbdc 0%,#8c9eb0 45%,#6a6a62 75%,#4a4d52 100%)}
  .equip .badge{left:519px;top:382px;width:142px;height:142px}
  .equip .copy{position:absolute;left:77px;top:93px;width:410px}
  .equip .copy p.note{margin-top:18px}
</style>
</head>
<body>

<section class="slide cover">
  <div class="photo" role="img" aria-label="Oil refinery tower and pipelines under a blue overcast sky, navy tinted"></div>
  <div class="brand"><i></i><span>NAVARO ENERGY</span></div>
</section>

<section class="slide why">
  <div class="photo" role="img" aria-label="Refinery processing tower with yellow walkways and pipelines"></div>
  <div class="bar"></div>
  <div class="copy">
    <h2>Why Choose Us?</h2>
    <p class="body">Lorem ipsum dolor sit amet, consectetur adipiscing elit. Nunc rutrum, orci molestie semper laoreet, quam leo commodo massa, in mollis sem urna et ante. In pretium, nibh eget semper dictum, eros libero sodales arcu, id tincidunt massa metus pretium eros.</p>
    <p class="body">Fusce vehicula dolor arcu, sit amet blandit dolor mollis nec. Donec viverra eleifend lacus, vitae ullamcorper metus. Sed sollicitudin ipsum quis nunc sollicitudin ultrices. Donec euismod scelerisque ligula. Maecenas eu varius risus, eu aliquet arcu. Curabitur fermentum suscipit est, tincidunt mattis lorem luctus id. Donec eget massa a diam condimentum pretium. Aliquam erat volutpat. Integer ut tincidunt orci.</p>
    <div class="stats">
      <div class="stat"><b>489+</b><span>Project Complete</span></div>
      <div class="stat"><b>250+</b><span>Company Trusted</span></div>
    </div>
    <p class="body note">Aliquam erat volutpat. Integer ut tincidunt orci. molestie semper laoreet, quam leo commodo massa</p>
  </div>
</section>

<section class="slide drill">
  <div class="photo p1" role="img" aria-label="Offshore drilling platform with cranes at sea"></div>
  <div class="photo p2" role="img" aria-label="Close view of offshore rig crane and deck"></div>
  <div class="badge">
    <svg width="70" height="70" viewBox="0 0 70 70" fill="none" stroke="#fff" stroke-width="3" stroke-linejoin="round"><path d="M35 12 C35 12 20 32 20 42 a15 15 0 0 0 30 0 C50 32 35 12 35 12Z"/></svg>
  </div>
  <div class="copy">
    <h2>Delivering innovative drilling solutions to unlock energy resources.</h2>
    <p class="body">Lorem ipsum dolor sit amet, consectetur adipiscing elit. Nunc rutrum, orci molestie semper laoreet, quam leo commodo massa, in mollis sem urna et ante. In pretium, nibh eget semper dictum, eros libero sodales arcu, id tincidunt massa metus pretium eros.</p>
    <p class="body" style="margin-top:20px">Fusce vehicula dolor arcu, sit amet blandit dolor mollis nec. Donec viverra eleifend lacus, vitae ullamcorper metus. Sed sollicitudin ipsum quis nunc sollicitudin ultrices. Donec euismod scelerisque ligula. Maecenas eu varius risus, eu aliquet arcu. Curabitur fermentum suscipit est, tincidunt mattis lorem luctus id. Donec eget massa a diam condimentum pretium. Aliquam erat volutpat. Integer ut tincidunt orci.</p>
  </div>
</section>

<section class="slide safety">
  <div class="photo p1" role="img" aria-label="Orange sunset sky over the sea"></div>
  <div class="photo p2" role="img" aria-label="Offshore worker in hard hat checking a tablet on deck at sunset"></div>
  <div class="copy">
    <h2>Committed to safety, efficiency, and superior operational performance.</h2>
    <p class="body">Lorem ipsum dolor sit amet, consectetur adipiscing elit. Nunc rutrum, orci molestie semper laoreet, quam leo commodo massa, in mollis sem urna et ante. In pretium.</p>
    <p class="body">Fusce vehicula dolor arcu, sit amet blandit dolor mollis nec. Donec viverra eleifend lacus, vitae ullamcorper metus. Sed sollicitudin ipsum quis nunc sollicitudin ultrices. Donec euismod scelerisque ligula. Maecenas eu varius risus, eu aliquet arcu. Curabitur fermentum suscipit est</p>
    <ul class="ticks">
      <li><svg width="32" height="32" viewBox="0 0 32 32" fill="none" stroke="var(--teal)" stroke-width="2.4" stroke-linecap="round" stroke-linejoin="round"><path d="M28 14.5V16a12 12 0 1 1-7-10.9"/><path d="M28 6 16 18l-4-4"/></svg>Deliver ultimate industrial services</li>
      <li><svg width="32" height="32" viewBox="0 0 32 32" fill="none" stroke="var(--teal)" stroke-width="2.4" stroke-linecap="round" stroke-linejoin="round"><path d="M28 14.5V16a12 12 0 1 1-7-10.9"/><path d="M28 6 16 18l-4-4"/></svg>No hidden extra charges needed</li>
    </ul>
  </div>
</section>

<section class="slide down">
  <div class="head">
    <h2>Downstream Oil and Gas Sector</h2>
    <p>Lorem ipsum dolor sit amet, consectetur adipiscing elit. Nunc rutrum, orci molestie semper laoreet, quam leo commodo massa. Fusce vehicula dolor arcu, sit amet blandit dolor mollis nec. Donec viverra eleifend lacus, vitae ullamcorper metus. Sed sollicitudin ipsum quis nunc sollicitudin ultrices. Donec euismod scelerisque ligula. Maecenas eu varius risus, eu aliquet arcu.</p>
  </div>
  <div class="photo" role="img" aria-label="Technician in orange hard hat working on plant valves and pipework"></div>
  <div class="copy">
    <h3>Navaro Downstream Sector</h3>
    <p>Fusce vehicula dolor arcu, sit amet blandit dolor lore mollis nec viverra dolor vitae viverra</p>
    <ul class="checks">
      <li><svg width="16" height="14" viewBox="0 0 16 14"><path d="M1.5 7.5 6 12 14.5 2" fill="none" stroke="var(--blue)" stroke-width="3" stroke-linecap="round" stroke-linejoin="round"/></svg>Oil Refining</li>
      <li><svg width="16" height="14" viewBox="0 0 16 14"><path d="M1.5 7.5 6 12 14.5 2" fill="none" stroke="var(--blue)" stroke-width="3" stroke-linecap="round" stroke-linejoin="round"/></svg>Supply and Trading</li>
      <li><svg width="16" height="14" viewBox="0 0 16 14"><path d="M1.5 7.5 6 12 14.5 2" fill="none" stroke="var(--blue)" stroke-width="3" stroke-linecap="round" stroke-linejoin="round"/></svg>Product Marketing</li>
      <li><svg width="16" height="14" viewBox="0 0 16 14"><path d="M1.5 7.5 6 12 14.5 2" fill="none" stroke="var(--blue)" stroke-width="3" stroke-linecap="round" stroke-linejoin="round"/></svg>Wholesale and Retail</li>
    </ul>
  </div>
</section>

<section class="slide equip">
  <div class="copy">
    <h2>Driving success with cutting-edge equipment and skilled professionals.</h2>
    <p class="body">Lorem ipsum dolor sit amet, consectetur adipiscing elit. Nunc rutrum, orci molestie semper laoreet, quam leo commodo massa, in mollis sem urna et ante. In pretium Aliquam erat volutpat. Integer ut tincidunt orci. molestie semper laoreet, quam leo commodo massa</p>
    <div class="stats">
      <div class="stat"><b>489+</b><span>Project Complete</span></div>
      <div class="stat"><b>250+</b><span>Company Trusted</span></div>
    </div>
    <p class="body note">Aliquam erat volutpat. Integer ut tincidunt orci. molestie semper laoreet, quam leo commodo massa</p>
  </div>
  <div class="photo" role="img" aria-label="Refinery processing tower with yellow walkways and pipelines"></div>
  <div class="badge">
    <svg width="64" height="64" viewBox="0 0 70 70" fill="#fff"><path d="M35 12 C35 12 20 32 20 42 a15 15 0 0 0 30 0 C50 32 35 12 35 12Z"/></svg>
  </div>
</section>

</body>
</html>
```